Brochure required for large legal practice

We require a brochure, poster and PowerPoint to be designed to promote our new Employee Benefits Program to our employees. The brochure needs to be modern, clean and corporate. Our target market is solicitors, legal support staff and administration staff based across multiple sites in Queensland, Australia. Logos and brochure/poster content have been attached as well as a detailed brief.

Please note that several photos of our employees have now been uploaded and can be used in this material only.                             

Legal

```html
<!DOCTYPE html>
<html lang="en">
<head>
<meta charset="utf-8">
<title>Harlow Group – Employee Benefits Program Brochure</title>
<link href="https://fonts.googleapis.com/css2?family=Lato:wght@300;400;700;900&display=swap" rel="stylesheet">
<style>
:root{
  --bg:#ececec;
  --ink:#1f1f1f;
  --paper:#ffffff;
  --text:#5a5a5a;
  --muted:#9a9a9a;
  --faint:#f2f2f2;
  --health:#8dc63f;
  --financial:#f7941d;
  --social:#1b75bb;
  --reward:#e0262b;
}
*{box-sizing:border-box;margin:0;padding:0}
html,body{width:1200px;height:3482px;overflow:hidden;background:var(--bg);font-family:"Lato",Arial,sans-serif;color:var(--text)}
.canvas{position:relative;width:1200px;height:3482px}
.page{position:absolute;width:288px;height:406px;background:var(--paper);box-shadow:0 1px 3px rgba(0,0,0,.12);overflow:hidden}
.page-footer{position:absolute;left:0;right:0;bottom:0;height:14px;background:var(--ink);font-size:4px;color:#8a8a8a;padding:5px 12px;letter-spacing:.3px}
.page-footer.right{text-align:right}
.brand{position:absolute;display:flex;align-items:center;gap:4px;font-size:6px;font-weight:700;letter-spacing:.6px;color:var(--ink);line-height:1}
.brand-mark{width:7px;height:7px;border:1.2px solid currentColor}
.brand.light{color:#ffffff}
.photo{position:absolute}
.title{position:absolute;font-weight:700;line-height:1.05;font-size:15px;letter-spacing:.2px}
.col{position:absolute}
.lead{font-size:5px;font-weight:700;color:#333;line-height:1.45;margin-bottom:5px}
.body{font-size:4.5px;line-height:1.55;color:var(--text);margin-bottom:4.5px}
.body b{color:#333}
.hl-health{color:var(--health);font-weight:700}
.hl-financial{color:var(--financial);font-weight:700}
.hl-reward{color:var(--reward);font-weight:700}
.subhead{font-size:4.6px;font-weight:900;color:#333;letter-spacing:.4px;margin-bottom:6px}
.ticks{list-style:none}
.ticks li{display:flex;gap:4px;font-size:4.5px;line-height:1.5;margin-bottom:5px;color:var(--text)}
.ticks svg{flex:none;width:6px;height:6px;margin-top:.5px}
.cover-top{position:absolute;left:0;top:0;width:100%;height:236px;background:var(--ink)}
.cover-title{position:absolute;right:12px;top:12px;color:#e6e6e6;font-weight:300;font-size:11px;line-height:1.3;text-align:right;letter-spacing:.3px}
.intro-title{position:absolute;left:14px;top:236px;font-size:13px;font-weight:400;color:var(--ink);line-height:1.25;letter-spacing:.3px}
.intro-rule{position:absolute;left:14px;top:272px;width:130px;height:1px;background:#dcdcdc}
.categories{position:absolute;left:14px;top:290px;font-size:4.3px;font-weight:700;letter-spacing:.3px}
.categories .sep{color:var(--muted);margin:0 3px}
.intro-notes{position:absolute;left:14px;top:308px;font-size:4.3px;color:var(--muted);line-height:2.6}
.decor-square{position:absolute;border:10px solid var(--faint)}
.back-contact{position:absolute;left:0;right:0;top:276px;text-align:center;color:#cfcfcf;font-size:4.3px;line-height:1.9}
.back-contact .label{color:#fff;font-weight:700;letter-spacing:.6px}
</style>
</head>
<body>
<main class="canvas">

  <!-- Front cover -->
  <section class="page cover" style="left:456px;top:28px">
    <div class="cover-top"></div>
    <h1 class="cover-title">EMPLOYEE BENEFITS<br>PROGRAM</h1>
    <div class="brand light" style="right:14px;top:214px"><span class="brand-mark"></span>HARLOW GROUP</div>
    <div class="photo" role="img" aria-label="Photo of four staff members in business attire standing in a bright office" style="left:0;top:236px;width:288px;height:170px;background:linear-gradient(180deg,#e2e2e2,#a3a3a3 50%,#3a3a3a)"></div>
  </section>

  <!-- Intro -->
  <section class="page intro" style="left:318px;top:453px">
    <div class="brand" style="left:14px;top:16px"><span class="brand-mark"></span>HARLOW GROUP</div>
    <div class="decor-square" style="left:118px;top:24px;width:74px;height:74px"></div>
    <h2 class="intro-title">EMPLOYEE BENEFITS<br>PROGRAM</h2>
    <div class="intro-rule"></div>
    <p class="categories">
      <span style="color:var(--health)">HEALTH</span><span class="sep">|</span><span style="color:var(--financial)">FINANCIAL</span><span class="sep">|</span><span style="color:var(--social)">SOCIAL &amp; COMMUNITY</span><span class="sep">|</span><span style="color:var(--reward)">REWARD &amp; RECOGNITION</span>
    </p>
    <p class="intro-notes">Your guide to staff benefits and rewards<br>Available to all employees across our Queensland offices<br>Speak with People and Culture for further details</p>
    <footer class="page-footer">harlowgroup.com.au</footer>
  </section>

  <!-- Program overview -->
  <section class="page overview" style="left:613px;top:453px">
    <div class="brand" style="right:14px;top:16px"><span class="brand-mark"></span>HARLOW GROUP</div>
    <h2 class="title" style="left:50px;top:86px;font-size:13px;font-weight:400;color:var(--ink)">PROGRAM OVERVIEW</h2>
    <div class="col" style="left:50px;top:108px;width:218px">
      <p class="body">Our Employee Benefits Program brings together a wide range of offers designed to support the health, finances and wellbeing of every member of our team. Whether you are a solicitor, a member of our legal support staff or part of our administration team, the program is open to you from your first day with the firm, at every one of our Queensland offices.</p>
      <p class="body">The program has been built around four key areas: <b>Health, Financial, Social &amp; Community and Reward &amp; Recognition.</b> Each section of this guide explains what is on offer, who is eligible and the simple steps you need to take to start using your benefits straight away.</p>
      <p class="body">We know that our people are the heart of our practice. By investing in your wellbeing, your financial security and your connection with colleagues, we aim to make our firm a great place to build a long and rewarding career.</p>
      <p class="body">Please read each section carefully, keep this guide handy, and speak with your manager or the People and Culture team if you have any questions about the program or your eligibility.</p>
    </div>
    <div class="decor-square" style="left:14px;top:300px;width:56px;height:56px"></div>
    <footer class="page-footer right">harlowgroup.com.au</footer>
  </section>

  <!-- Health -->
  <section class="page health" style="left:318px;top:875px">
    <div class="brand" style="left:14px;top:16px"><span class="brand-mark"></span>HARLOW GROUP</div>
    <div class="decor-square" style="left:106px;top:22px;width:60px;height:60px"></div>
    <div class="photo" role="img" aria-label="Photo of a red apple" style="left:146px;top:18px;width:62px;height:68px;background:radial-gradient(circle at 45% 55%,#e03a2a,#9c1410 64%,#fff 67%)"></div>
    <h2 class="title" style="left:14px;top:116px;color:var(--health)">HEALTH</h2>
    <div class="col" style="left:14px;top:138px;width:108px">
      <p class="lead">Staying well at work and at home matters to every one of us.</p>
      <p class="body">All employees can access discounted private health insurance through our preferred provider, with reduced waiting periods and no joining fee for new members.</p>
      <p class="body">Free annual flu vaccinations are offered at each office, along with yearly health checks covering blood pressure, cholesterol and skin screening.</p>
      <p class="body">Our <span class="hl-health">Employee Assistance Program</span> provides free, confidential counselling for you and your immediate family members.</p>
    </div>
    <div class="photo" role="img" aria-label="Photo of a healthy meal" style="left:136px;top:162px;width:58px;height:32px;background:linear-gradient(135deg,#c9a07a,#6d8a3e)"></div>
    <div class="photo" role="img" aria-label="Photo of fitness equipment" style="left:198px;top:162px;width:72px;height:32px;background:linear-gradient(135deg,#4d6f9c,#d6c25b)"></div>
    <div class="photo" role="img" aria-label="Photo of a health check consultation" style="left:136px;top:197px;width:58px;height:32px;background:linear-gradient(135deg,#d8c7b6,#7c6656)"></div>
    <div class="photo" role="img" aria-label="Photo of a staff member exercising" style="left:198px;top:197px;width:72px;height:32px;background:linear-gradient(135deg,#a9b9c9,#5a5a5a)"></div>
    <div class="col" style="left:136px;top:240px;width:134px">
      <p class="lead">Fitness and wellbeing support for every employee.</p>
      <p class="body">Enjoy subsidised gym memberships at a network of centres close to each office, plus a weekly fruit delivery and free ergonomic workstation assessments.</p>
      <p class="body">Join our <span class="hl-health">lunchtime walking groups</span> or the annual corporate fun run, and claim up to four wellbeing days each year.</p>
    </div>
    <div class="photo" role="img" aria-label="Photo of two colleagues smiling in the office" style="left:14px;top:268px;width:108px;height:80px;background:linear-gradient(180deg,#dfe3e6,#6f6f72)"></div>
    <footer class="page-footer">harlowgroup.com.au</footer>
  </section>

  <!-- Financial -->
  <section class="page financial" style="left:613px;top:875px">
    <div class="brand" style="left:14px;top:16px"><span class="brand-mark"></span>HARLOW GROUP</div>
    <h2 class="title" style="left:144px;top:14px;color:var(--financial)">FINANCIAL</h2>
    <div class="col" style="left:144px;top:36px;width:128px">
      <p class="lead">Make your salary go further with a range of financial benefits.</p>
      <p class="body">Salary packaging lets you pay for items such as a car, laptop or extra superannuation from your pre-tax salary, which could reduce the amount of tax you pay.</p>
      <p class="body">Our payroll team can model how <span class="hl-financial">salary sacrifice and novated leasing</span> would work for you before you make any decision.</p>
      <p class="body">Staff also have access to discounted home loans, fee-free everyday accounts and reduced insurance premiums through our banking partner.</p>
    </div>
    <div class="col" style="left:14px;top:120px;width:112px">
      <p class="subhead">FEATURED BENEFITS</p>
      <ul class="ticks">
        <li><svg viewBox="0 0 6 6"><path d="M1 3l1.5 1.5L5 1.5" fill="none" stroke="var(--financial)" stroke-width="1"/></svg>Salary packaging and novated leasing options for all permanent staff</li>
        <li><svg viewBox="0 0 6 6"><path d="M1 3l1.5 1.5L5 1.5" fill="none" stroke="var(--financial)" stroke-width="1"/></svg>Discounted banking and home loan products</li>
        <li><svg viewBox="0 0 6 6"><path d="M1 3l1.5 1.5L5 1.5" fill="none" stroke="var(--financial)" stroke-width="1"/></svg>Free annual session with a licensed financial planner</li>
        <li><svg viewBox="0 0 6 6"><path d="M1 3l1.5 1.5L5 1.5" fill="none" stroke="var(--financial)" stroke-width="1"/></svg>Retail discounts on travel, groceries and entertainment</li>
      </ul>
    </div>
    <div class="photo" role="img" aria-label="Photo of payment cards" style="left:46px;top:262px;width:76px;height:38px;background:linear-gradient(135deg,#e4cf7a,#5b8fc1)"></div>
    <div class="photo" role="img" aria-label="Photo of a smiling staff member in a suit" style="left:150px;top:214px;width:118px;height:136px;background:linear-gradient(180deg,#cfd3d6,#2f3236)"></div>
    <footer class="page-footer right">harlowgroup.com.au</footer>
  </section>

  <!-- Social & Community -->
  <section class="page social" style="left:318px;top:1297px">
    <div class="brand" style="left:14px;top:16px"><span class="brand-mark"></span>HARLOW GROUP</div>
    <div class="photo" role="img" aria-label="Photo of a group of staff standing together" style="left:126px;top:10px;width:118px;height:112px;background:linear-gradient(180deg,#f4f4f4,#8a8a8a)"></div>
    <h2 class="title" style="left:14px;top:90px;color:var(--social)">SOCIAL &amp;<br>COMMUNITY</h2>
    <div class="col" style="left:14px;top:134px;width:112px">
      <p class="lead">Connect with colleagues and give back to the community.</p>
      <ul class="ticks">
        <li><svg viewBox="0 0 6 6"><path d="M1 3l1.5 1.5L5 1.5" fill="none" stroke="var(--health)" stroke-width="1"/></svg>Social club events at every office throughout the year</li>
        <li><svg viewBox="0 0 6 6"><path d="M1 3l1.5 1.5L5 1.5" fill="none" stroke="var(--health)" stroke-width="1"/></svg>One day of paid volunteer leave for each employee every year</li>
        <li><svg viewBox="0 0 6 6"><path d="M1 3l1.5 1.5L5 1.5" fill="none" stroke="var(--health)" stroke-width="1"/></svg>Workplace giving with matched donations to approved charities</li>
        <li><svg viewBox="0 0 6 6"><path d="M1 3l1.5 1.5L5 1.5" fill="none" stroke="var(--health)" stroke-width="1"/></svg>Pro bono legal work supporting local community groups</li>
      </ul>
    </div>
    <div class="col" style="left:144px;top:134px;width:128px">
      <p class="lead">Staff come together across all of our sites.</p>
      <p class="body">Our social club organises end of financial year celebrations, family days, trivia nights and the annual end of year party, with events held in every region.</p>
      <p class="body">Join one of our <span class="hl-health">social sporting teams</span> or take part in charity drives and fundraising days organised by staff.</p>
      <p class="body">New starters are paired with a buddy to help them settle in and meet colleagues across the firm.</p>
    </div>
    <div class="photo" role="img" aria-label="Photo of two colleagues outdoors with a city skyline" style="left:14px;top:266px;width:204px;height:82px;background:linear-gradient(180deg,#b9c3cc,#7d868c 60%,#4a4f52)"></div>
    <footer class="page-footer">harlowgroup.com.au</footer>
  </section>

  <!-- Reward and Recognition -->
  <section class="page reward" style="left:613px;top:1297px">
    <div class="brand" style="left:14px;top:16px"><span class="brand-mark"></span>HARLOW GROUP</div>
    <h2 class="title" style="left:144px;top:14px;color:var(--reward)">REWARD AND<br>RECOGNITION</h2>
    <div class="col" style="left:144px;top:52px;width:128px">
      <p class="lead">Recognising the people who make our firm great.</p>
      <p class="body">Each year we celebrate outstanding contributions to our clients, our colleagues and our community through a firm-wide awards program.</p>
      <p class="body"><span class="hl-reward">Nominations open in March</span> and any employee can put forward a colleague or team whose work deserves recognition.</p>
      <p class="body">Winners are announced at our annual awards evening and receive a gift voucher, extra leave and a certificate.</p>
    </div>
    <div class="photo" role="img" aria-label="Photo of two staff members at an awards presentation" style="left:22px;top:48px;width:108px;height:160px;background:linear-gradient(180deg,#3a6fb5,#1d3f78)"></div>
    <div class="photo" role="img" aria-label="Photo of gold trophies" style="left:44px;top:230px;width:60px;height:62px;background:radial-gradient(circle at 50% 45%,#f0c34a,#a67712 58%,#fff 61%)"></div>
    <ul class="ticks col" style="left:136px;top:232px;width:136px">
      <li><svg viewBox="0 0 6 6"><circle cx="3" cy="3" r="3" fill="var(--social)"/></svg>Annual excellence awards across practice and support teams</li>
      <li><svg viewBox="0 0 6 6"><circle cx="3" cy="3" r="3" fill="var(--health)"/></svg>Long service recognition at five, ten and twenty years</li>
      <li><svg viewBox="0 0 6 6"><circle cx="3" cy="3" r="3" fill="var(--financial)"/></svg>Peer nomination program with monthly thank you vouchers</li>
      <li><svg viewBox="0 0 6 6"><circle cx="3" cy="3" r="3" fill="var(--reward)"/></svg>Team achievement bonuses for major matters and milestones</li>
    </ul>
    <footer class="page-footer right">harlowgroup.com.au</footer>
  </section>

  <!-- Back cover -->
  <section class="page back" style="left:456px;top:1722px">
    <div class="cover-top" style="height:366px"></div>
    <div class="back-contact">
      <div class="brand light" style="position:static;justify-content:center;margin-bottom:6px"><span class="brand-mark"></span></div>
      <p class="label">CONTACT</p>
      <p>Harlow Group Employee Benefits Program</p>
      <p>People and Culture Team</p>
      <p>benefits@harlowgroup.com.au</p>
    </div>
    <div class="brand" style="left:14px;top:384px"><span class="brand-mark"></span>HARLOW GROUP</div>
  </section>

</main>
</body>
</html>
```